PLUM BUSINESS CARD

Need a business card and logo. The company name is PLUM (Piedmont League of Ultimate Mareriders). It's a business that offers horseback riding lessons to young girls. Please put my name: Renata Bowley and a place for email and phone number. I would like the card to look feminine and soft. I like script type lettering. I want the card to be white or ivory with black or gray and hot pink print. A horse head outline would be cool, something whimsical. Think teen girl who likes glamour. Also, I give western riding lessons. So I like faded out background Images of western saddles, cowgirls, horses with long hair, ropes, horses in sunset...mabe the word PLUM can be made out of a lasso rope?

Just updated my project with a little more detail

Target Market(s)

Young girls/ cowgirls, western riding

Industry/Entity Type

Horseback Riding

Font styles to use
Script

Colors
e34197

Requirements
Must have
• A logo of PLUM.
Must say Piedmont League of Ultimate Mareriders
Colors are Pink and Black with an elegant, glamorous, feminine look.
Nice to have
• Could have a picture or outline of a horse

```html
<!DOCTYPE html>
<html lang="en">
<head>
<meta charset="utf-8">
<title>PLUM Business Card</title>
<link rel="stylesheet" href="https://fonts.googleapis.com/css2?family=Cormorant+Garamond:ital,wght@0,600;1,500;1,600&display=swap">
<style>
  :root {
    --pink-top: #fd8cef;
    --pink-mid: #ffc9f4;
    --ivory: #eff5e3;
    --hot-pink: #f548a8;
    --logo-pink: #ee4aae;
    --ink: #1b1216;
    --silhouette: #111111;
  }
  * { margin: 0; padding: 0; box-sizing: border-box; }
  html, body {
    width: 1200px;
    height: 686px;
    overflow: hidden;
    background: var(--ivory);
  }
  .card {
    position: relative;
    width: 1200px;
    height: 686px;
    overflow: hidden;
    background: linear-gradient(180deg,
      var(--pink-top) 0%,
      var(--pink-top) 22%,
      var(--pink-mid) 36%,
      var(--ivory) 50%,
      var(--ivory) 100%);
    font-family: "Cormorant Garamond", "Times New Roman", serif;
    font-style: italic;
    color: var(--ink);
  }
  .brand-name {
    position: absolute;
    left: 0;
    top: 18px;
    width: 1200px;
    text-align: center;
    font-family: "Cormorant Garamond", "Times New Roman", serif;
    font-style: normal;
    font-weight: 600;
    font-size: 150px;
    line-height: 150px;
    letter-spacing: 24px;
    color: var(--logo-pink);
  }
  .tagline {
    position: absolute;
    left: 0;
    top: 172px;
    width: 1200px;
    text-align: center;
    font-size: 38px;
    line-height: 44px;
    font-weight: 600;
  }
  .rider-artwork {
    position: absolute;
    left: 436px;
    top: 232px;
    width: 284px;
    height: 282px;
    border-radius: 40% 45% 20% 20%;
    background: radial-gradient(ellipse at 50% 55%, #2a2a2a 0%, var(--silhouette) 70%);
  }
  .band {
    position: absolute;
    left: 0;
    width: 1200px;
    background: var(--hot-pink);
  }
  .band--name { top: 528px; height: 53px; }
  .band--contact { top: 611px; height: 48px; }
  .holder-name {
    position: absolute;
    left: 103px;
    top: 528px;
    height: 53px;
    line-height: 53px;
    font-size: 44px;
    font-weight: 500;
  }
  .contact {
    position: absolute;
    top: 611px;
    height: 48px;
    line-height: 48px;
    font-size: 33px;
    font-weight: 500;
  }
  .contact--phone { left: 96px; }
  .contact--email { left: 651px; }
</style>
</head>
<body>
  <main class="card">
    <h1 class="brand-name">PLUM</h1>
    <p class="tagline">Piedmont League of Ultimate Mareriders</p>

    <div class="rider-artwork" role="img" aria-label="Black silhouette of a rider on a walking horse wearing a pink halter"></div>

    <div class="band band--name"></div>
    <div class="band band--contact"></div>

    <p class="holder-name">Renata Bowley</p>
    <p class="contact contact--phone">Phone Number: (xxx)xxx-xxxx</p>
    <p class="contact contact--email">Email: sample@email.com</p>
  </main>
</body>
</html>
```